Webdesign für Branchenverzeichnis
Zielgruppe
Wir-bauen-Brücken – das Branchenverzeichnis der Selbstverantwortlichen.
Der Anbieter präsentiert sich mit seinem Namen und der URL - ähnlich wie bei 'blaue Blätter' oder Torkwerk.
Aufgabenstellung
Das Branchenverzeichnis sollte neutral und gleichzeitig hochwertig sein. Die Hauptfarben sind Gold, Schwarz und Weiß. Logo und Corporate Design wurden bereits entwickelt

```html
<!DOCTYPE html>
<html lang="de">
<head>
<meta charset="utf-8">
<title>Wir bauen Brücken – Branchenverzeichnis</title>
<link href="https://fonts.googleapis.com/css2?family=Quicksand:wght@400;500;600;700&display=swap" rel="stylesheet">
<style>
:root{
  --gold:#d6b266;
  --gold-light:#e9d5a6;
  --cream:#fefae8;
  --hero-bg:#fbfbfb;
  --ink:#111;
  --text:#555;
  --dark:#3e3e3e;
  --white:#fff;
}
*{margin:0;padding:0;box-sizing:border-box}
html,body{width:1025px;height:1200px;overflow:hidden}
body{position:relative;font-family:'Quicksand',sans-serif;background:var(--cream);color:var(--ink)}
.abs{position:absolute}
.header{left:0;top:0;width:1025px;height:53px;background:linear-gradient(#3d3d3d,#6a6a6a)}
.brand{left:134px;top:12px;display:flex;align-items:center;gap:6px;color:var(--gold);font-weight:700;font-size:9.5px;line-height:11px;white-space:nowrap}
.brand .dot{width:18px;height:18px;border-radius:50%;border:2px solid var(--gold);flex:none}
.nav a{position:absolute;top:21px;color:var(--white);font-size:7.5px;font-weight:700;letter-spacing:1px;text-decoration:none}
.nav a.active{color:var(--gold)}
.icon-box{top:16px;width:21px;height:21px;border:1px solid var(--gold);display:flex;align-items:center;justify-content:center}
.header-cta{left:784px;top:14px;width:107px;height:24px;background:var(--gold);color:var(--white);font-size:6.5px;font-weight:600;letter-spacing:.8px;display:flex;align-items:center;justify-content:center}
.hero{left:0;top:53px;width:1025px;height:360px;background:var(--hero-bg)}
.hero-title{left:137px;top:113px;font-size:28px;font-weight:700;letter-spacing:2px}
.hero-title span,.section-title span{color:var(--gold)}
.hero-sub{left:137px;top:148px;font-size:13.5px;letter-spacing:.6px;color:#222}
.hero-text{left:137px;top:173px;width:480px;font-size:9.3px;line-height:14.5px;color:#777;letter-spacing:.45px}
.btn{top:258px;height:33px;display:flex;align-items:center;justify-content:center;font-size:8.5px;letter-spacing:.6px}
.btn-primary{left:137px;width:133px;background:var(--gold);color:var(--white)}
.btn-outline{left:302px;width:109px;border:1px solid var(--gold-light);color:#333;background:var(--white)}
.hero-photo{left:680px;top:53px}
.search{left:133px;top:360px;width:758px;height:107px;background:var(--gold);box-shadow:0 6px 14px rgba(0,0,0,.12)}
.field{top:37px;width:160px;height:32px;background:var(--white);border:1px solid #e8e3d4;display:flex;align-items:center;justify-content:space-between;padding:0 11px;font-size:9px;color:#666}
.search-btn{left:620px;top:37px;width:107px;height:32px;background:var(--dark);color:var(--white);font-size:7px;font-weight:600;letter-spacing:.6px;display:flex;align-items:center;justify-content:center}
.section-title{left:0;width:1025px;top:510px;text-align:center;font-size:24px;font-weight:700;letter-spacing:3px}
.section-sub{left:0;width:1025px;top:543px;text-align:center;font-size:12.5px;letter-spacing:1.3px;color:#333}
.card{width:130px;height:134px;background:var(--gold-light);box-shadow:0 2px 5px rgba(0,0,0,.08);text-align:center}
.card.active{background:#fffef4;border:1px solid var(--gold-light)}
.card svg{margin-top:27px}
.card h3{margin-top:14px;font-size:13.5px;font-weight:500;letter-spacing:.8px}
.card p{margin-top:2px;font-size:7.8px;letter-spacing:.7px;color:#555}
.footer{left:0;top:968px;width:1025px;height:232px;background:linear-gradient(#6d6d6d,#2f2f2f);color:var(--white)}
.f-brand{left:219px;top:66px;width:55px;height:55px;border-radius:50%;border:2px solid var(--white);display:flex;align-items:center;justify-content:center;text-align:center;font-size:7px;font-weight:700;line-height:9px}
.f-about{left:307px;top:68px;width:165px}
.f-about h4{font-size:9.5px;font-weight:700;margin-bottom:9px}
.f-about p{font-size:7.8px;line-height:13px;color:#eee}
.f-about a{display:block;margin-top:4px;font-size:8px;color:var(--gold)}
.f-col h4{font-size:9.5px;font-weight:700;letter-spacing:.4px;margin-bottom:8px}
.f-col li{list-style:none;font-size:7.8px;line-height:21.3px;color:#eee}
.copy{left:0;width:1025px;top:1173px;text-align:center;font-size:6.5px;font-weight:600;color:#eee}
</style>
</head>
<body>
<header class="abs header">
  <div class="abs brand"><span class="dot"></span><span>Wir bauen<br>Brücken</span></div>
  <nav class="nav">
    <a class="active" style="left:245px">HOME</a>
    <a style="left:310px">SUCHEN</a>
    <a style="left:384px">ÜBER UNS</a>
    <a style="left:465px">MITGLIEDSCHAFT</a>
    <a style="left:577px">KONTAKT</a>
  </nav>
  <div class="abs icon-box" style="left:703px">
    <svg width="15" height="10" viewBox="0 0 15 9"><rect width="15" height="3" fill="#000"/><rect y="3" width="15" height="3" fill="#d00"/><rect y="6" width="15" height="3" fill="#fc0"/></svg>
  </div>
  <div class="abs icon-box" style="left:732px">
    <svg width="11" height="11" viewBox="0 0 10 10" fill="#d6b266"><circle cx="5" cy="3" r="2.3"/><path d="M0.5 10c0-3 2-4.3 4.5-4.3S9.5 7 9.5 10z"/></svg>
  </div>
  <div class="abs header-cta">MITGLIED WERDEN</div>
</header>

<section class="abs hero"></section>
<svg class="abs hero-photo" width="345" height="360" viewBox="0 0 345 360" role="img" aria-label="Foto: zwei Personen sitzen auf einem Steg am nebligen See">
  <defs>
    <linearGradient id="lake" x1="0" y1="0" x2="0" y2="1">
      <stop offset="0" stop-color="#f2f2f0"/>
      <stop offset=".55" stop-color="#e3e2de"/>
      <stop offset=".8" stop-color="#b9b0a6"/>
      <stop offset="1" stop-color="#a59c92"/>
    </linearGradient>
  </defs>
  <path d="M86 0H345V360H60C30 310 10 260 10 200C10 120 40 50 86 0Z" fill="url(#lake)"/>
  <path d="M86 0C40 50 10 120 10 200C10 260 30 310 60 360" fill="none" stroke="#fbf0c8" stroke-width="6"/>
  <path d="M80 0C34 52 4 120 4 200C4 262 24 312 54 360" fill="none" stroke="#d6b266" stroke-width="3"/>
</svg>

<h1 class="abs hero-title">WIR BAUEN <span>BRÜCKEN</span></h1>
<p class="abs hero-sub">Das Branchenverzeichnis der Selbstverantwortlichen</p>
<p class="abs hero-text">Lorem ipsum dolor sit amet, consectetur adipisicing elit, sed do eiusmod tempor incididunt ut labore et dolore magna aliqua. Duis aute irure dolor in reprehenderit in voluptate velit esse cillum dolore eu fugiat nulla pariatur. Ut enim ad minim veniam, quis nostrud exercitation ullamco laboris nisi ut aliquip ex ea commodo!</p>
<div class="abs btn btn-primary">UNTERNEHMER SUCHEN</div>
<div class="abs btn btn-outline">MITGLIED WERDEN</div>

<form class="abs search">
  <div class="abs field" style="left:33px">Unternehmen, Name
    <svg width="15" height="14" viewBox="0 0 16 14" fill="#d6b266"><path d="M8 0L16 7H13.5V14H10V9.5H6V14H2.5V7H0Z"/></svg></div>
  <div class="abs field" style="left:219px">Stadt, PLZ oder Land
    <svg width="15" height="15" viewBox="0 0 16 16" fill="none" stroke="#d6b266" stroke-width="1.5"><circle cx="8" cy="8" r="5"/><circle cx="8" cy="8" r="2" fill="#d6b266"/><path d="M8 0v3M8 13v3M0 8h3M13 8h3"/></svg></div>
  <div class="abs field" style="left:406px">Branche
    <svg width="12" height="8" viewBox="0 0 12 8" fill="none" stroke="#d6b266" stroke-width="1.8"><path d="M1 1l5 5 5-5"/></svg></div>
  <div class="abs search-btn">SUCHEN</div>
</form>

<h2 class="abs section-title">WIR ZEIGEN <span>BRANCHEN</span></h2>
<p class="abs section-sub">Top 10 der gesuchten Unternehmenszweige.</p>

<svg width="0" height="0" style="position:absolute">
  <symbol id="people" viewBox="0 0 54 36">
    <circle cx="16" cy="8" r="7.5"/><circle cx="37" cy="8" r="7"/>
    <path d="M0 36C0 24 7 19 16 19S32 24 32 36Z"/>
    <path d="M35 36C35 28 33 23 30 20.5C32 19.5 34.5 19 37 19C46 19 54 24 54 36Z"/>
  </symbol>
</svg>

<div class="abs card" style="left:139px;top:599px"><svg width="54" height="36" fill="#fff"><use href="#people"/></svg><h3>Coaching</h3><p>(23 Unternehmen)</p></div>
<div class="abs card active" style="left:296px;top:599px"><svg width="54" height="36" fill="#d6b266"><use href="#people"/></svg><h3>Consulting</h3><p>(14 Unternehmen)</p></div>
<div class="abs card" style="left:453px;top:599px"><svg width="54" height="36" fill="#fff"><use href="#people"/></svg><h3>IT &amp; Marketing</h3><p>(23 Unternehmen)</p></div>
<div class="abs card" style="left:610px;top:599px"><svg width="54" height="36" fill="#fff"><use href="#people"/></svg><h3>Logistik</h3><p>(23 Unternehmen)</p></div>
<div class="abs card" style="left:767px;top:599px"><svg width="54" height="36" fill="#fff"><use href="#people"/></svg><h3>Bildung</h3><p>(23 Unternehmen)</p></div>

<div class="abs card" style="left:139px;top:775px"><svg width="54" height="36" fill="#fff"><use href="#people"/></svg><h3>Coaching</h3><p>(23 Unternehmen)</p></div>
<div class="abs card" style="left:296px;top:775px"><svg width="54" height="36" fill="#fff"><use href="#people"/></svg><h3>Coaching</h3><p>(23 Unternehmen)</p></div>
<div class="abs card" style="left:453px;top:775px"><svg width="54" height="36" fill="#fff"><use href="#people"/></svg><h3>IT &amp; Marketing</h3><p>(23 Unternehmen)</p></div>
<div class="abs card" style="left:610px;top:775px"><svg width="54" height="36" fill="#fff"><use href="#people"/></svg><h3>Logistik</h3><p>(23 Unternehmen)</p></div>
<div class="abs card" style="left:767px;top:775px"><svg width="54" height="36" fill="#fff"><use href="#people"/></svg><h3>Bildung</h3><p>(23 Unternehmen)</p></div>

<footer class="abs footer">
  <div class="abs f-brand">Wir bauen<br>Brücken</div>
  <div class="abs f-about">
    <h4>Wir bauen Brücken</h4>
    <p>Duis sed odio sit amet nibh vulputate cursus a sit amet mauris. Morbi accumsan ipsum velit. Nam nec tellus a</p>
    <a>Über uns</a>
  </div>
  <div class="abs f-col" style="left:553px;top:67px">
    <h4>WEBSITE</h4>
    <ul><li>Wir bauen Brücken</li><li>Unternehmen suchen</li><li>Mitgliedschaft</li><li>Kontakt</li></ul>
  </div>
  <div class="abs f-col" style="left:717px;top:67px">
    <h4>RECHTLICHES</h4>
    <ul><li>Impressum</li><li>Datenschutz</li><li>AGB</li><li>Sicherheitsbestimmungen</li></ul>
  </div>
</footer>
<p class="abs copy">© 2020 Wir bauen Brücken</p>
</body>
</html>
```